Facebook Cover & Profile Branding for VelbrooK Systems

We need a modern, premium Facebook cover image for our company Velbrook Systems GmbH. The design should be clean, professional, and aligned with our corporate colors (neon green and deep blue) as well as our logo. It should clearly represent us as a technology and IT consulting company with a strong focus on software testing and quality assurance.

Since Velbrook Systems is also active in the U.S. market, the design may include global or U.S.-related elements (e.g., subtle references to international presence, tech innovation with a global reach).

Requirements:

Integration of the Velbrook logo and brand colors

Modern, premium look with a tech-driven feel

Clear, simple layout that looks good on desktop and mobile

Optional: subtle U.S./international references to highlight our global presence

Goal:
A professional, eye-catching Facebook cover image that strengthens our brand identity and reflects our international expansion into the U.S. market.

Target Market(s)

Medium to large enterprises in the technology, finance, and energy sectors - Companies looking for premium IT consulting, software testing, and quality assurance services - Decision makers and executives (CIOs, CTOs, IT managers) in Europe and the United States - A global audience that values innovation, professionalism, and trust

Industry/Entity Type

Information Technology & Consulting Software Testing & Quality Assurance Technology / Professional Services Global IT Consulting with U.S. Market Presence

Requirements
Must have
• Integration of the Velbrook Systems logo and brand colors (Neon Green & Deep Blue) Modern, premium design with a strong tech-oriented look and feel Clean and professional layout, optimized for both desktop and mobile display Clear visibility of the brand identity (technology, IT consulting, software testing, quality assurance) Subtle reference to U.S. presence / global expansion (to highlight activity in both Germany and the U.S.) Balanced use of colors and space for a high-end, corporate appearance
Nice to have
• Subtle animations or motion effects (e.g., light gradients, moving lines, glowing accents) Dark/Light version option for different moods or seasonal campaigns Integration of social media icons (LinkedIn, Instagram, Facebook) in a clean, minimal way Tech-inspired background elements (digital patterns, abstract shapes, network grids) Space for an optional tagline or slogan (e.g., “Innovation. Quality. Global Impact.”) Adaptability for other platforms (so the design style can be reused for LinkedIn or Twitter headers)
Should not have
• Cluttered or overloaded layouts that reduce clarity Low-quality stock photos or generic imagery that doesn’t fit a premium brand Use of colors outside the Velbrook brand identity (Neon Green & Deep Blue) Outdated design styles (e.g., heavy gradients, 3D effects, drop shadows) Complex text blocks that make the design look busy Elements that distract from the logo and core brand message Pop-art or playful styles that don’t match the premium, professional tech look

```html
<!DOCTYPE html>
<html lang="en">
<head>
<meta charset="utf-8">
<title>Velbrook Systems – Facebook Cover &amp; Profile Branding</title>
<link rel="stylesheet" href="https://fonts.googleapis.com/css2?family=Inter:wght@400;500;600&amp;display=swap">
<style>
  :root {
    --page: #ececec;
    --card: #12161c;
    --card-edge: #1a1f27;
    --green: #8ee03c;
    --blue: #2f8fe3;
    --blue-soft: #3aa3ee;
    --text: #f2f4f7;
    --text-muted: #c9ced6;
  }
  * { margin: 0; padding: 0; box-sizing: border-box; }
  html, body {
    width: 1200px;
    height: 655px;
    overflow: hidden;
    background: var(--page);
  }
  .board {
    position: relative;
    width: 1200px;
    height: 655px;
    font-family: "Inter", Arial, sans-serif;
  }
  .card {
    position: absolute;
    display: block;
    background: var(--card);
  }
  .card--cover   { left: 64px;  top: 115px; width: 636px; height: 395px; }
  .card--mobile  { left: 767px; top: 75px;  width: 348px; height: 222px; }
  .card--profile { left: 764px; top: 338px; width: 356px; height: 224px; }
  .card text { font-family: "Inter", Arial, sans-serif; }
  .brand-name   { fill: var(--text); font-weight: 600; }
  .brand-sub    { fill: var(--text); font-weight: 600; }
  .brand-dot    { fill: var(--green); }
  .headline     { fill: var(--text); font-weight: 500; }
  .spec         { fill: var(--text-muted); font-weight: 400; }
  .hex-code     { fill: var(--text); font-weight: 400; }
  .service      { fill: var(--text-muted); font-weight: 400; }
  .frame-green  { fill: none; stroke: var(--green); stroke-linejoin: miter; }
  .frame-blue   { fill: none; stroke: var(--blue); stroke-linejoin: miter; }
  .band-blue    { fill: var(--blue); }
  .band-green   { fill: var(--green); }
  .accent-dash  { stroke: var(--green); }
  .divider      { stroke: var(--blue); }
  .icon-ring    { fill: var(--blue-soft); }
  .icon-cut     { stroke: var(--card); fill: none; }
</style>
</head>
<body>
<main class="board">

  <!-- Cover -->
  <svg class="card card--cover" viewBox="0 0 747 463" role="img" aria-label="Velbrook Systems Facebook cover">
    <rect width="747" height="463" fill="var(--card)"/>
    <rect x="380" y="0" width="367" height="463" fill="var(--card-edge)" opacity="0.5"/>

    <g class="brand">
      <circle class="brand-dot" cx="58" cy="62" r="16"/>
      <text class="brand-name" x="86" y="62" font-size="23">Velbrook</text>
      <text class="brand-sub" x="86" y="82" font-size="13">Systems GmbH</text>
    </g>

    <polyline class="frame-green" stroke-width="7" points="617,96 482,96 457,121 457,205"/>
    <polyline class="frame-blue" stroke-width="7" points="703,166 716,179 716,262 665,312 612,312"/>

    <g class="brand brand--center">
      <text class="brand-name" x="585" y="202" font-size="23" text-anchor="middle">Velbrook</text>
      <text class="brand-sub" x="585" y="222" font-size="13" text-anchor="middle">Systems GmbH</text>
    </g>

    <text class="headline" x="38" y="254" font-size="26">Empowering Technology.</text>
    <text class="headline" x="38" y="290" font-size="26">Enabling Success.</text>

    <line class="accent-dash" x1="38" y1="346" x2="98" y2="346" stroke-width="3"/>

    <g class="spec-icon">
      <circle class="icon-ring" cx="58" cy="395" r="17"/>
      <path class="icon-cut" stroke-width="3" d="M46 383 L70 407 M70 383 L46 407"/>
    </g>
    <text class="spec" x="90" y="392" font-size="18">820×312 px</text>
    <text class="spec" x="90" y="416" font-size="18">Cover and 1000 px</text>

    <polygon class="band-blue" points="505,463 747,262 747,305 560,463"/>
    <polygon class="band-green" points="560,463 700,330 747,330 747,463"/>
    <polygon class="band-blue" points="0,383 78,463 0,463"/>
  </svg>

  <!-- Mobile cover -->
  <svg class="card card--mobile" viewBox="0 0 408 261" role="img" aria-label="Velbrook Systems mobile cover">
    <rect width="408" height="261" fill="var(--card)"/>

    <g class="brand">
      <circle class="brand-dot" cx="27" cy="42" r="9"/>
      <text class="brand-name" x="42" y="42" font-size="13">Velbrook</text>
      <text class="brand-sub" x="42" y="53" font-size="8">Systems GmbH</text>
    </g>

    <polyline class="frame-green" stroke-width="4" points="330,59 265,59 249,75 249,131"/>
    <polyline class="frame-blue" stroke-width="4" points="378,97 392,110 392,150 366,177 300,177"/>

    <text class="hex-code" x="292" y="122" font-size="11">#00D4FF</text>

    <text class="headline" x="18" y="142" font-size="14">Empowering Technology.</text>
    <text class="headline" x="18" y="160" font-size="14">Enabling Success.</text>

    <line class="accent-dash" x1="18" y1="191" x2="53" y2="191" stroke-width="2"/>

    <g class="spec-icon">
      <circle class="icon-ring" cx="30" cy="221" r="10"/>
      <path class="icon-cut" stroke-width="2" d="M23 214 L37 228 M37 214 L23 228"/>
    </g>
    <text class="spec" x="52" y="218" font-size="11">830×314 px</text>
    <text class="spec" x="52" y="233" font-size="11">Cover and 1000 px</text>

    <polygon class="band-blue" points="276,261 408,158 408,190 318,261"/>
    <polygon class="band-green" points="318,261 378,205 408,205 408,261"/>
    <polygon class="band-blue" points="0,216 42,261 0,261"/>
  </svg>

  <!-- Profile -->
  <svg class="card card--profile" viewBox="0 0 418 263" role="img" aria-label="Velbrook Systems profile premium card">
    <rect width="418" height="263" fill="var(--card)"/>

    <g class="brand">
      <circle class="brand-dot" cx="30" cy="37" r="9"/>
      <text class="brand-name" x="45" y="38" font-size="13">Velbrook</text>
      <text class="brand-sub" x="45" y="49" font-size="8">Systems GmbH</text>
    </g>

    <polyline class="frame-green" stroke-width="4" points="338,54 272,54 255,71 255,126"/>
    <polyline class="frame-blue" stroke-width="4" points="386,92 400,106 400,150 372,178 306,178"/>

    <text class="hex-code" x="296" y="120" font-size="11">#00D4FF</text>

    <text class="headline" x="22" y="126" font-size="20">Profile Premium</text>

    <line class="accent-dash" x1="22" y1="176" x2="58" y2="176" stroke-width="2"/>

    <g class="services services--left">
      <text class="service" x="22" y="199" font-size="10.5">Consulting</text>
      <text class="service" x="22" y="213" font-size="10.5">Software Testing</text>
      <text class="service" x="22" y="227" font-size="10.5">International</text>
      <text class="service" x="22" y="241" font-size="10.5">Europe &amp; USA</text>
    </g>
    <line class="divider" x1="130" y1="190" x2="130" y2="215" stroke-width="1.5"/>
    <g class="services services--right">
      <text class="service" x="138" y="199" font-size="10.5">IT Consulting &amp;</text>
      <text class="service" x="138" y="213" font-size="10.5">Software Testing</text>
      <text class="service" x="138" y="227" font-size="10.5">International Clients</text>
      <text class="service" x="138" y="241" font-size="10.5">USA</text>
    </g>

    <polygon class="band-blue" points="284,263 418,160 418,192 326,263"/>
    <polygon class="band-green" points="326,263 386,207 418,207 418,263"/>
    <polygon class="band-blue" points="0,222 40,263 0,263"/>
  </svg>

</main>
</body>
</html>
```